Engineering Land Development Company Needs Flyer Brochure for Prospective Professional Clients

Our company provides land development site design for commercial projects. We have many repeat clients that are familiar with our work. We do not advertise our services other than a website. Most of our referrals are from existing clients. When a new client contacts us and asks for a proposal for a project we would like to have a brochure that shows our strengths, experience, and professionalism. We are selling professional services similar to a lawyer or accountant. We want new clients to feel comfortable hiring a new firm. The brochure would be one page single-side included when we submit proposals for new projects. Check out our website at tovarnix.com for more info. We would like a brochure that mixes grading/excavation construction work on a job site with business professional. We will need to update the brochure so we want it in .doc .psd or some other edit format. The brochure we are using is attached. It is very two-dimensional. We need some depth.

Target Market(s)

Land developers, architects, real estate, professionals, attorneys

Industry/Entity Type

Real Estate Development

Font styles to use
Sans Serif
Other font styles liked:
• calibri

Colors
0355a3
9bcb3c

Requirements
Must have
• company logo, ability to update text and images
Nice to have
• background image(s) with text overlay
Should not have
• cartoons, harsh colors, stock photos of people, lots of boxes

```html
<!DOCTYPE html>
<html lang="en">
<head>
<meta charset="utf-8">
<title>Tovarnix Engineering PLLC – Flyer</title>
<link href="https://fonts.googleapis.com/css2?family=Open+Sans:wght@400;600;700&display=swap" rel="stylesheet">
<style>
  :root{
    --blue:#0355a3;
    --green:#9bcb3c;
    --green-deep:#4f9a4a;
    --teal:#3d8a78;
    --ink:#2c2c2c;
    --paper:#ffffff;
    --mist:#e4e9ee;
  }
  *{margin:0;padding:0;box-sizing:border-box}
  html,body{width:833px;height:1200px;overflow:hidden;background:var(--paper)}
  body{font-family:"Open Sans",Arial,sans-serif;color:var(--ink);position:relative}
  .flyer{position:absolute;inset:0;background:var(--paper)}
  .site-backdrop{position:absolute;left:0;top:590px;width:833px;height:540px;
    background:
      radial-gradient(ellipse 60% 70% at 80% 60%,rgba(150,165,180,.35),transparent 70%),
      linear-gradient(180deg,rgba(255,255,255,1) 0,rgba(226,232,238,.9) 35%,#d6dde4 100%)}
  .brand{position:absolute;top:30px;right:22px;display:flex;align-items:center;gap:8px}
  .brand-mark{width:22px;height:22px;background:var(--blue)}
  .brand-name{font-size:19px;font-weight:600;color:var(--blue);letter-spacing:-.3px}
  .hero{position:absolute;left:0;top:70px;width:833px;height:460px}
  .mission{position:absolute;left:0;top:436px;width:790px;text-align:center;color:#fff;font-weight:600;font-size:19px;line-height:30px;text-shadow:0 1px 3px rgba(0,0,0,.35)}
  .intro{position:absolute;left:30px;top:548px;width:780px;font-size:10.4px;line-height:14px}
  .service{position:absolute;left:30px;width:780px;height:108px;display:flex;gap:12px}
  .service-thumb{width:158px;height:100px;flex:none;border:3px solid #fff;box-shadow:0 3px 8px rgba(0,0,0,.35)}
  .service-body{flex:1}
  .service-tab{display:inline-block;background:linear-gradient(90deg,var(--green-deep),var(--teal));color:#fff;font-weight:700;font-size:11px;padding:2px 22px 2px 6px;border-radius:0 12px 12px 0;letter-spacing:.3px;box-shadow:0 1px 3px rgba(0,0,0,.25)}
  .service-title{color:var(--blue);font-weight:700;font-size:9.4px;margin:8px 0 2px}
  .service-text{font-size:9.4px;line-height:13.5px}
  .footer{position:absolute;left:0;bottom:0;width:833px;height:75px;background:var(--blue);color:#fff;box-shadow:0 -3px 8px rgba(0,0,0,.2)}
  .call{position:absolute;left:0;top:0;width:300px;height:75px;background:linear-gradient(90deg,var(--teal),var(--green));border-radius:0 42px 42px 0;text-align:center;font-weight:700;line-height:27px;padding-top:9px;box-shadow:3px 0 8px rgba(0,0,0,.25)}
  .call-label{font-size:28px;margin-left:30px}
  .call-number{font-size:26px;display:flex;align-items:center;justify-content:center;gap:8px}
  .footer-col{position:absolute;top:21px;font-size:12px;line-height:16px;display:flex;gap:8px}
  .footer-divider{position:absolute;left:555px;top:16px;width:1px;height:44px;background:rgba(255,255,255,.7)}
  .footer-mark{position:absolute;right:20px;top:17px;width:40px;height:40px;background:#fff}
</style>
</head>
<body>
<div class="flyer">
  <div class="site-backdrop" role="img" aria-label="Faint photo of a building structure under construction behind the service list"></div>

  <div class="brand"><span class="brand-mark"></span><span class="brand-name">Tovarnix Engineering PLLC</span></div>

  <svg class="hero" viewBox="0 0 833 460">
    <defs>
      <linearGradient id="sky" x1="0" y1="0" x2="0" y2="1">
        <stop offset="0" stop-color="#1f5fc8"/><stop offset=".35" stop-color="#3f86e0"/>
        <stop offset=".52" stop-color="#8fbdf0"/><stop offset=".6" stop-color="#c99c62"/>
        <stop offset=".8" stop-color="#b27a45"/><stop offset="1" stop-color="#8f5f38"/>
      </linearGradient>
      <radialGradient id="trees" cx=".12" cy=".52" r=".3">
        <stop offset="0" stop-color="#2f5a24" stop-opacity=".95"/><stop offset=".6" stop-color="#4a7a34" stop-opacity=".6"/><stop offset="1" stop-color="#4a7a34" stop-opacity="0"/>
      </radialGradient>
      <radialGradient id="machine" cx=".55" cy=".42" r=".35">
        <stop offset="0" stop-color="#e6b428" stop-opacity=".75"/><stop offset=".7" stop-color="#d9a530" stop-opacity=".25"/><stop offset="1" stop-color="#d9a530" stop-opacity="0"/>
      </radialGradient>
      <radialGradient id="bucket" cx=".4" cy=".6" r=".22">
        <stop offset="0" stop-color="#a8683a" stop-opacity=".8"/><stop offset="1" stop-color="#a8683a" stop-opacity="0"/>
      </radialGradient>
      <linearGradient id="band" x1="0" y1="0" x2="1" y2="0">
        <stop offset="0" stop-color="#3d8a78" stop-opacity=".9"/><stop offset="1" stop-color="#9bcb3c" stop-opacity=".9"/>
      </linearGradient>
      <linearGradient id="shade" x1="0" y1="0" x2="0" y2="1">
        <stop offset="0" stop-color="#000" stop-opacity="0"/><stop offset="1" stop-color="#000" stop-opacity=".25"/>
      </linearGradient>
      <clipPath id="heroShape"><path d="M0 20 H700 A90 90 0 0 1 790 110 V362 A80 80 0 0 1 710 442 H0 Z"/></clipPath>
      <filter id="lift" x="-5%" y="-5%" width="110%" height="115%"><feDropShadow dx="0" dy="4" stdDeviation="5" flood-opacity=".3"/></filter>
    </defs>
    <line x1="0" y1="10" x2="833" y2="10" stroke="var(--green)" stroke-width="3"/>
    <line x1="0" y1="16" x2="833" y2="16" stroke="var(--blue)" stroke-width="2"/>
    <path d="M690 8 A112 112 0 0 1 812 120 V362 A92 92 0 0 1 720 454" fill="none" stroke="var(--blue)" stroke-width="6"/>
    <g clip-path="url(#heroShape)" filter="url(#lift)">
      <g role="img" aria-label="Photo of a yellow excavator digging on a sandy job site beside a tree line under a blue sky">
        <rect x="0" y="20" width="800" height="422" fill="url(#sky)"/>
        <rect x="0" y="20" width="800" height="422" fill="url(#trees)"/>
        <rect x="0" y="20" width="800" height="422" fill="url(#machine)"/>
        <rect x="0" y="20" width="800" height="422" fill="url(#bucket)"/>
        <rect x="0" y="250" width="800" height="192" fill="url(#shade)"/>
      </g>
      <rect x="0" y="352" width="800" height="90" fill="url(#band)"/>
    </g>
  </svg>
  <p class="mission">Our mission at Tovarnix Engineering is to provide Superior Quality<br>Professional Land Development Services</p>

  <p class="intro">Our firm provides planning, surveying, engineering, and environmental services which allows us to focus on the entire land development process rather than one specific discipline. Providing a broad scope of professional services helps to streamline a project by eliminating many disadvantages of having multiple firms with overlapping responsibilities.</p>

  <section class="service" style="top:622px">
    <div class="service-thumb" role="img" aria-label="Aerial photo of a development site" style="background:radial-gradient(circle at 30% 40%,#c9c2ae,transparent 55%),radial-gradient(circle at 75% 70%,#5d6e4e,transparent 60%),linear-gradient(135deg,#a3a48e,#6d7762)"></div>
    <div class="service-body">
      <span class="service-tab">PLANNING</span>
      <p class="service-title">We are land development professionals who can see the "big picture".</p>
      <p class="service-text">We have extensive experience with site selection, due diligence investigations, re-zonings, and land planning. Every project is different. We look forward to identifying all feasible alternatives. We become part of the project and enjoy developing the best plan for the success of each particular project. We understand that time is money and unexpected delays are unacceptable.</p>
    </div>
  </section>

  <section class="service" style="top:746px">
    <div class="service-thumb" role="img" aria-label="Photo of a GPS survey instrument on a tripod against blue sky" style="background:radial-gradient(ellipse 25% 45% at 45% 75%,#c8402e,transparent 70%),radial-gradient(circle at 45% 35%,#3a3a3a,transparent 18%),linear-gradient(180deg,#1d59c0,#4d8ae0 80%,#7da8e8)"></div>
    <div class="service-body">
      <span class="service-tab">SURVEYING</span>
      <p class="service-title">We are land development professionals who provide superior quality surveying services.</p>
      <p class="service-text">Our firm can handle any surveying need. We have extensive experience with ALTA surveys, boundary surveys, subdivision platting, topographic/location surveys, GPS surveys, R/W surveys, construction staking, as-built surveys, elevation certificates, etc. We work closely with title attorneys to provide legal descriptions, exhibits, and other assistance when closing the real estate deal.</p>
    </div>
  </section>

  <section class="service" style="top:870px">
    <div class="service-thumb" role="img" aria-label="Engineering site drawing in blue linework" style="background:radial-gradient(circle at 35% 40%,#eef0fc,transparent 60%),linear-gradient(135deg,#d3d6f4,#8e96dd)"></div>
    <div class="service-body">
      <span class="service-tab">ENGINEERING</span>
      <p class="service-title">We are land development professionals who can handle the most complicated engineering challenge.</p>
      <p class="service-text">Let us worry about all the technical stuff and the regulators. Our firm has extensive experience with infrastructure assessments, erosion control, grading, roadway design, stormwater management, water systems, sewer systems, utilities, flood plain management, landscape design, permitting, bidding, and construction administration.</p>
    </div>
  </section>

  <section class="service" style="top:994px">
    <div class="service-thumb" role="img" aria-label="Photo of green trees reflected in a calm pond" style="background:radial-gradient(ellipse 60% 30% at 65% 40%,#5f9a2e,transparent 75%),linear-gradient(180deg,#d8e6f2 0,#b9cfe0 22%,#5c8c36 42%,#3f6a2c 58%,#6d8a5a 72%,#9fb0b0 100%)"></div>
    <div class="service-body">
      <span class="service-tab">ENVIRONMENTAL</span>
      <p class="service-title">We are land development professionals who provide superior quality environmental services.</p>
      <p class="service-text">We provide environmental site assessments, underground storage tank management, soil and groundwater sampling and testing, contamination remediation, Brownfields assessments, permitting and redevelopment, and wetlands permitting. Our firm works closely with state and federal agencies to provide economical mitigation and remediation solutions.</p>
    </div>
  </section>

  <footer class="footer">
    <div class="call">
      <div class="call-label">CALL US</div>
      <div class="call-number">
        <svg width="24" height="24" viewBox="0 0 24 24" fill="none" stroke="#fff" stroke-width="2"><circle cx="12" cy="12" r="10.5"/><path d="M8 6.5l2 2.5-1.2 1.5a7 7 0 0 0 4.7 4.7l1.5-1.2 2.5 2-1.3 1.7c-4.5 0-9.7-5.2-9.7-9.7z" fill="#fff" stroke="none"/></svg>
        555.204.7310
      </div>
    </div>
    <div class="footer-col" style="left:330px">
      <svg width="11" height="15" viewBox="0 0 12 16"><path d="M6 0a6 6 0 0 1 6 6c0 4-6 10-6 10S0 10 0 6a6 6 0 0 1 6-6z" fill="#fff"/><circle cx="6" cy="6" r="2.2" fill="#0355a3"/></svg>
      <span>418 Ridgeway Avenue-Suite 300<br>Larkston, NC 27014</span>
    </div>
    <span class="footer-divider"></span>
    <div class="footer-col" style="left:580px">
      <svg width="12" height="32" viewBox="0 0 12 32"><rect x="0" y="3" width="12" height="8" rx="1" fill="#fff"/><path d="M0 3l6 5 6-5" stroke="#0355a3" fill="none"/><circle cx="6" cy="24" r="5" fill="none" stroke="#fff" stroke-width="1.5"/><path d="M1 24h10M6 19v10" stroke="#fff"/></svg>
      <span>info@tovarnix.com<br>www.tovarnix.com</span>
    </div>
    <span class="footer-mark"></span>
  </footer>
</div>
</body>
</html>
```